Simple Webpage for Company that offer IT Security Services

Company Type: Penetration Tests, IT Security Services, Security Audits
Company Name: VaultHaven
Navigation Style: similar to https://www.brivanta-example.com/en/ with Top Navigation (and submenu's)
Top Navigation Items: Services, About Us, Contact
Industry/Entity Type
It Company
Coding
Coded - Design and coding required

```html
<!DOCTYPE html>
<html lang="en">
<head>
<meta charset="UTF-8">
<title>VaultHaven – IT Security Services</title>
<link rel="stylesheet" href="https://fonts.googleapis.com/css2?family=Roboto:wght@300;400;500;700;900&display=swap">
<style>
  :root {
    --blue: #1d72b8;
    --blue-bright: #2a86d0;
    --band: #2379c0;
    --ink: #25313d;
    --text: #4a525a;
    --muted: #7b838b;
    --light: #eef0f2;
    --card-border: #d3d6d9;
    --footer: #2e3135;
    --white: #ffffff;
  }
  * { box-sizing: border-box; margin: 0; padding: 0; }
  html, body { width: 1200px; height: 2304px; overflow: hidden; }
  body { font-family: "Roboto", Arial, sans-serif; color: var(--text); background: var(--white); position: relative; }

  .site-header { position: absolute; top: 0; left: 0; width: 1200px; height: 80px; background: var(--white); display: flex; align-items: center; padding: 0 40px; }
  .brand { font-weight: 900; font-size: 28px; letter-spacing: 0.5px; color: var(--blue); }
  .main-nav { margin-left: auto; display: flex; align-items: center; height: 80px; }
  .main-nav a { display: flex; align-items: center; height: 80px; padding: 0 26px; font-size: 15px; font-weight: 500; letter-spacing: 1px; color: var(--ink); text-decoration: none; position: relative; }
  .main-nav a.active { color: var(--blue); }
  .main-nav a.active::before { content: ""; position: absolute; left: 14px; right: 14px; top: 0; height: 4px; background: var(--blue); }
  .nav-icon { width: 56px; display: flex; justify-content: center; }

  .hero { position: absolute; top: 80px; left: 0; width: 1200px; height: 480px; background: radial-gradient(ellipse at 60% 55%, #2f6fb0 0%, #153a66 40%, #0a1a33 75%, #060f20 100%); }
  .hero-content { position: absolute; left: 130px; top: 178px; width: 420px; }
  .hero h1 { font-size: 38px; line-height: 42px; font-weight: 700; color: var(--white); text-transform: uppercase; }
  .hero p { margin-top: 16px; font-size: 13px; line-height: 17px; color: #dce6f2; }

  .btn { display: inline-block; height: 32px; line-height: 32px; padding: 0 44px; border-radius: 16px; background: var(--blue); color: var(--white); font-size: 13px; font-weight: 500; text-decoration: none; text-align: center; }
  .hero .btn { margin-top: 22px; width: 176px; padding: 0; }

  .features { position: absolute; top: 560px; left: 0; width: 1200px; height: 640px; background: var(--light); }
  .card { position: absolute; top: 180px; width: 272px; height: 420px; background: var(--white); border: 3px solid var(--card-border); box-shadow: 0 4px 10px rgba(0,0,0,0.08); text-align: center; padding: 88px 34px 0; }
  .card:nth-child(1) { left: 100px; }
  .card:nth-child(2) { left: 464px; }
  .card:nth-child(3) { left: 812px; }
  .card-icon { position: absolute; top: -30px; left: 50%; transform: translateX(-50%); }
  .card h3 { font-size: 15px; font-weight: 700; color: var(--ink); text-transform: uppercase; }
  .card p { margin-top: 16px; font-size: 12.5px; line-height: 16px; color: var(--text); }
  .card .btn { position: absolute; bottom: 40px; left: 50%; transform: translateX(-50%); width: 120px; padding: 0; height: 28px; line-height: 28px; font-size: 12px; }

  .service-band { position: absolute; top: 1200px; left: 0; width: 1200px; height: 140px; background: var(--band); display: flex; justify-content: space-around; align-items: center; padding: 0 60px; }
  .service-item { display: flex; align-items: center; gap: 18px; color: var(--white); font-size: 20px; font-weight: 500; text-transform: uppercase; }

  .about { position: absolute; top: 1340px; left: 0; width: 1200px; height: 430px; background: var(--white); }
  .about-text { position: absolute; left: 112px; top: 152px; width: 460px; }
  .about h2 { font-size: 30px; font-weight: 900; color: var(--blue); }
  .about p { margin-top: 14px; font-size: 12.5px; line-height: 16px; color: var(--text); }
  .about .btn { margin-top: 26px; width: 176px; padding: 0; }
  .about-visual { position: absolute; left: 680px; top: 50px; width: 400px; height: 340px; border-radius: 12px; background: linear-gradient(180deg, #2b8ad6 0%, #1d72b8 60%, #e8eef5 61%, #ffffff 100%); }

  .stats { position: absolute; top: 1770px; left: 0; width: 1200px; height: 440px; background: var(--light); text-align: center; }
  .stats h2 { margin-top: 16px; font-size: 23px; font-weight: 300; color: var(--muted); }
  .stat { position: absolute; top: 80px; width: 280px; text-align: center; }
  .stat:nth-child(2) { left: 92px; }
  .stat:nth-child(3) { left: 460px; }
  .stat:nth-child(4) { left: 820px; }
  .stat-ring { position: relative; width: 160px; height: 160px; margin: 0 auto; }
  .stat-ring span { position: absolute; inset: 0; display: flex; align-items: center; justify-content: center; font-size: 40px; font-weight: 400; color: var(--ink); }
  .stat h3 { margin-top: 10px; font-size: 20px; font-weight: 500; color: var(--blue); text-transform: uppercase; }
  .stat p { margin-top: 6px; font-size: 12.5px; line-height: 16px; color: var(--text); }

  .site-footer { position: absolute; top: 2210px; left: 0; width: 1200px; height: 94px; background: var(--footer); text-align: center; padding-top: 24px; }
  .site-footer .brand { color: var(--white); font-size: 28px; }
  .site-footer small { display: block; margin-top: 4px; font-size: 11px; color: #9aa0a6; }
</style>
</head>
<body>

<header class="site-header">
  <div class="brand">VAULTHAVEN</div>
  <nav class="main-nav">
    <a href="#" class="active">HOME</a>
    <a href="#">SERVICES</a>
    <a href="#">ABOUT US</a>
    <a href="#">CONTACT</a>
    <span class="nav-icon">
      <svg width="16" height="16" viewBox="0 0 16 16"><circle cx="6.5" cy="6.5" r="5" fill="none" stroke="#25313d" stroke-width="2"/><line x1="10.5" y1="10.5" x2="15" y2="15" stroke="#25313d" stroke-width="2"/></svg>
    </span>
    <span class="nav-icon">
      <svg width="18" height="14" viewBox="0 0 18 14"><rect y="0" width="18" height="2" fill="#25313d"/><rect y="6" width="18" height="2" fill="#25313d"/><rect y="12" width="18" height="2" fill="#25313d"/></svg>
    </span>
  </nav>
</header>

<section class="hero" role="img" aria-label="Photo of a data centre aisle with rows of illuminated server racks">
  <div class="hero-content">
    <h1>Lorem ipsum is<br>just dummy text</h1>
    <p>Lorem ipsum dolor sit amet, consectetur adipiscing elit, sed do eiusmod tempor incididunt ut labore et dolore magna aliqua. Ut enim ad minim veniam, quis nostrud exercitation.</p>
    <a href="#" class="btn">Learn More</a>
  </div>
</section>

<section class="features">
  <article class="card">
    <svg class="card-icon" width="60" height="60" viewBox="0 0 60 60"><circle cx="30" cy="30" r="30" fill="#1d72b8"/><ellipse cx="30" cy="19" rx="12" ry="4" fill="#fff"/><path d="M18 19v22c0 2.2 5.4 4 12 4s12-1.8 12-4V19" fill="none" stroke="#fff" stroke-width="2.5"/><path d="M18 27c0 2.2 5.4 4 12 4s12-1.8 12-4M18 34c0 2.2 5.4 4 12 4s12-1.8 12-4" fill="none" stroke="#fff" stroke-width="2.5"/></svg>
    <h3>Lorem ipsum title</h3>
    <p>Lorem ipsum dolor sit amet, consectetur adipiscing elit, sed do eiusmod tempor incididunt ut labore et dolore magna aliqua. Ut enim ad minim veniam, quis nostrud exercitation ullamco laboris nisi ut aliquip ex ea commodo consequat. Duis aute irure dolor in reprehenderit.</p>
    <a href="#" class="btn">Learn More</a>
  </article>
  <article class="card">
    <svg class="card-icon" width="60" height="60" viewBox="0 0 60 60"><circle cx="30" cy="30" r="30" fill="#1d72b8"/><ellipse cx="30" cy="19" rx="12" ry="4" fill="#fff"/><path d="M18 19v22c0 2.2 5.4 4 12 4s12-1.8 12-4V19" fill="none" stroke="#fff" stroke-width="2.5"/><path d="M18 27c0 2.2 5.4 4 12 4s12-1.8 12-4M18 34c0 2.2 5.4 4 12 4s12-1.8 12-4" fill="none" stroke="#fff" stroke-width="2.5"/></svg>
    <h3>Lorem ipsum title</h3>
    <p>Lorem ipsum dolor sit amet, consectetur adipiscing elit, sed do eiusmod tempor incididunt ut labore et dolore magna aliqua. Ut enim ad minim veniam, quis nostrud exercitation ullamco laboris nisi ut aliquip ex ea commodo consequat. Duis aute irure dolor in reprehenderit.</p>
    <a href="#" class="btn">Learn More</a>
  </article>
  <article class="card">
    <svg class="card-icon" width="60" height="60" viewBox="0 0 60 60"><circle cx="30" cy="30" r="30" fill="#1d72b8"/><ellipse cx="30" cy="19" rx="12" ry="4" fill="#fff"/><path d="M18 19v22c0 2.2 5.4 4 12 4s12-1.8 12-4V19" fill="none" stroke="#fff" stroke-width="2.5"/><path d="M18 27c0 2.2 5.4 4 12 4s12-1.8 12-4M18 34c0 2.2 5.4 4 12 4s12-1.8 12-4" fill="none" stroke="#fff" stroke-width="2.5"/></svg>
    <h3>Lorem ipsum title</h3>
    <p>Lorem ipsum dolor sit amet, consectetur adipiscing elit, sed do eiusmod tempor incididunt ut labore et dolore magna aliqua. Ut enim ad minim veniam, quis nostrud exercitation ullamco laboris nisi ut aliquip ex ea commodo consequat. Duis aute irure dolor in reprehenderit.</p>
    <a href="#" class="btn">Learn More</a>
  </article>
</section>

<section class="service-band">
  <div class="service-item">
    <svg width="40" height="30" viewBox="0 0 40 30"><rect x="2" y="6" width="36" height="18" rx="4" fill="none" stroke="#fff" stroke-width="2.5"/><line x1="2" y1="16" x2="38" y2="16" stroke="#fff" stroke-width="2"/><circle cx="31" cy="20" r="1.8" fill="#fff"/></svg>
    <span>Important Service</span>
  </div>
  <div class="service-item">
    <svg width="44" height="32" viewBox="0 0 44 32"><path d="M12 26h-2a8 8 0 0 1 0-16 11 11 0 0 1 21-2 9 9 0 0 1 3 18h-2" fill="none" stroke="#fff" stroke-width="2.5"/><path d="M22 30V16M17 21l5-5 5 5" fill="none" stroke="#fff" stroke-width="2.5"/></svg>
    <span>Important Service</span>
  </div>
  <div class="service-item">
    <svg width="36" height="36" viewBox="0 0 36 36"><circle cx="18" cy="18" r="6" fill="none" stroke="#fff" stroke-width="2.5"/><path d="M18 3v6M18 27v6M3 18h6M27 18h6M7.4 7.4l4.2 4.2M24.4 24.4l4.2 4.2M7.4 28.6l4.2-4.2M24.4 11.6l4.2-4.2" stroke="#fff" stroke-width="2.5"/></svg>
    <span>Important Service</span>
  </div>
</section>

<section class="about">
  <div class="about-text">
    <h2>VAULTHAVEN</h2>
    <p>VaultHaven Lorem ipsum dolor sit amet, consectetur adipiscing elit, sed do eiusmod tempor incididunt ut labore et dolore magna aliqua. Ut enim ad minim veniam, quis nostrud exercitation ullamco laboris nisi ut aliquip ex ea commodo consequat. Duis aute irure dolor in reprehenderit in voluptate velit esse cillum dolore eu fugiat nulla pariatur. Excepteur sint occaecat cupidatat non proident, sunt in culpa qui officia deserunt mollit anim id est laborum.</p>
    <a href="#" class="btn">Learn More</a>
  </div>
  <div class="about-visual" role="img" aria-label="Illustration of a blue cloud holding server units connected to network nodes"></div>
</section>

<section class="stats">
  <h2>Our customers value our expertise and vast project experience of over</h2>
  <div class="stat">
    <div class="stat-ring">
      <svg width="160" height="160" viewBox="0 0 160 160"><circle cx="80" cy="80" r="74" fill="none" stroke="#c9ced3" stroke-width="2"/><circle cx="80" cy="80" r="62" fill="#fff" stroke="#1d72b8" stroke-width="8" stroke-dasharray="300 90" transform="rotate(-90 80 80)"/></svg>
      <span>850</span>
    </div>
    <h3>Lorem ipsum</h3>
    <p>Lorem ipsum dolor sit amet,<br>consectetur adipiscing elit, sed do.</p>
  </div>
  <div class="stat">
    <div class="stat-ring">
      <svg width="160" height="160" viewBox="0 0 160 160"><circle cx="80" cy="80" r="74" fill="none" stroke="#c9ced3" stroke-width="2"/><circle cx="80" cy="80" r="62" fill="#fff" stroke="#1d72b8" stroke-width="8" stroke-dasharray="300 90" transform="rotate(-90 80 80)"/></svg>
      <span>120</span>
    </div>
    <h3>Lorem ipsum</h3>
    <p>Lorem ipsum dolor sit amet,<br>consectetur adipiscing elit, sed do.</p>
  </div>
  <div class="stat">
    <div class="stat-ring">
      <svg width="160" height="160" viewBox="0 0 160 160"><circle cx="80" cy="80" r="74" fill="none" stroke="#c9ced3" stroke-width="2"/><circle cx="80" cy="80" r="62" fill="#fff" stroke="#1d72b8" stroke-width="8" stroke-dasharray="300 90" transform="rotate(-90 80 80)"/></svg>
      <span>500</span>
    </div>
    <h3>Lorem ipsum</h3>
    <p>Lorem ipsum dolor sit amet,<br>consectetur adipiscing elit, sed do.</p>
  </div>
</section>

<footer class="site-footer">
  <div class="brand">VAULTHAVEN</div>
  <small>© 2024 VaultHaven. All rights reserved.</small>
</footer>

</body>
</html>
```